Brennick Holdings Business Cards

These are professional business cards that are for my family office.
Put fake emails and phone numbers as of now until I finalize those components. This family office controls my families investments, assets, and future. The cards should be professional.
..
.
.
.
I just uploaded another variation of a logo I would like to see as a business card to I am inbeteen which logo to use

Target Market(s)

business

Industry/Entity Type

business

Contact Information for Business Card

Professional, wealth related, finance related.

Requirements
Must have
• Logo

```html
<!DOCTYPE html>
<html lang="en">
<head>
<meta charset="utf-8">
<title>Brennick Holdings Business Cards</title>
<link rel="stylesheet" href="https://fonts.googleapis.com/css2?family=Cinzel:wght@500&family=Tinos&display=swap">
<style>
  :root {
    --backdrop: #e3e4e7;
    --navy: #1b2131;
    --navy-soft: #2b3346;
    --paper: #ffffff;
    --silver: #a9abb0;
    --ink-light: #eef0f4;
  }
  * { box-sizing: border-box; margin: 0; padding: 0; }
  html, body { width: 1200px; height: 800px; overflow: hidden; }
  body {
    background: var(--backdrop);
    display: flex;
    align-items: center;
    justify-content: center;
    gap: 70px;
    font-family: "Tinos", serif;
  }
  .card {
    position: relative;
    width: 525px;
    height: 300px;
    overflow: hidden;
    box-shadow: 0 10px 28px rgba(20, 24, 36, 0.18);
  }
  /* Front side */
  .card--front {
    background: linear-gradient(150deg, var(--navy-soft), var(--navy) 70%);
  }
  .front-name {
    position: absolute;
    left: 42px;
    top: 46px;
    font-family: "Cinzel", serif;
    font-weight: 500;
    font-size: 30px;
    letter-spacing: 1px;
    color: var(--ink-light);
  }
  .front-seal {
    position: absolute;
    right: 44px;
    bottom: -30px;
    width: 210px;
    height: 210px;
    border-radius: 50%;
    border: 3px solid rgba(255, 255, 255, 0.07);
    background: rgba(255, 255, 255, 0.03);
  }
  /* Back side */
  .card--back { background: var(--paper); }
  .back-shape { position: absolute; inset: 0; }
  .back-brand {
    position: absolute;
    left: 34px;
    top: 34px;
    display: flex;
    align-items: center;
    gap: 12px;
  }
  .brand-dot {
    width: 40px; height: 40px;
    border-radius: 50%;
    border: 2px solid var(--navy);
  }
  .brand-name {
    font-family: "Cinzel", serif;
    font-weight: 500;
    font-size: 20px;
    color: var(--navy);
  }
  .contact {
    position: absolute;
    right: 30px;
    top: 122px;
    text-align: right;
    color: var(--ink-light);
    font-size: 13px;
    line-height: 1.3;
  }
  .contact-name {
    font-size: 17px;
    letter-spacing: 1px;
    color: var(--silver);
  }
  .contact-title { margin-bottom: 14px; }
  .contact-line { display: flex; justify-content: flex-end; align-items: center; gap: 6px; }
  .contact-line svg { width: 11px; height: 11px; flex: none; }
  .address { margin-bottom: 8px; }
</style>
</head>
<body>
  <div class="card card--front">
    <div class="front-name">Brennick Holdings</div>
    <div class="front-seal"></div>
  </div>

  <div class="card card--back">
    <svg class="back-shape" viewBox="0 0 525 300" aria-hidden="true">
      <circle cx="470" cy="330" r="225" fill="var(--navy)"/>
      <path d="M 260 330 A 240 240 0 0 1 400 100" fill="none" stroke="var(--navy)" stroke-width="6"/>
      <path d="M 430 92 A 240 240 0 0 1 525 100" fill="none" stroke="var(--navy)" stroke-width="6"/>
    </svg>
    <div class="back-brand">
      <span class="brand-dot"></span>
      <span class="brand-name">Brennick Holdings</span>
    </div>
    <div class="contact">
      <div class="contact-name">DANIEL HART</div>
      <div class="contact-title">Director</div>
      <div class="address">00 dummy city<br>dummy place 0000</div>
      <div class="contact-line">555-014-2760
        <svg viewBox="0 0 12 12"><path d="M3 1 L5 3 L4 5 Q5 7 7 8 L9 7 L11 9 L9 11 Q4 10 1 3 Z" fill="var(--silver)"/></svg>
      </div>
      <div class="contact-line">info@brennickholdings.com
        <svg viewBox="0 0 12 12"><rect x="1" y="3" width="10" height="7" fill="var(--silver)"/><path d="M1 3 L6 7 L11 3" fill="none" stroke="var(--navy)"/></svg>
      </div>
      <div class="contact-line">www.brennickholdings.com
        <svg viewBox="0 0 12 12"><circle cx="6" cy="6" r="5" fill="none" stroke="var(--silver)"/><path d="M1 6 H11 M6 1 V11" stroke="var(--silver)"/></svg>
      </div>
    </div>
  </div>
</body>
</html>
```